Web-page design

We need a initial web design for our page kavilora.com.au (which is not yet set up).
We provide consulting services for all kinds of problems in and between organisations.
Main focus is on conflict resolution but we also support companies on improving their operational performance.
We want to have the following page structure (and part of the project is to design the 8 pages):
- Home
- Services (we offer 3 main service areas - one per page)
- Case studies (one per page)
- Engaging us (our process)
- About Conflict & low performance
- Conflict resolution App
- About
- Contact (Email form)
- Our logo should be on each page.
The start page should include the following information:
- Twitter / Linkedin / facebook/ google + Links
- Telephone / Email or in general contact details
- News
- A quite prominent picture box with 3 alternating pics - each representing one of our service areas
- Link to our App
- Testimonials
It would be nice if the service pages would have an image header. Links to the information section (about conflict & low performance; and the app page) would be nice as well.
We like the following joomla designs: www.quorbixlane.com/itempreview/153
No need to copy it, it should just give you an idea.
We like the layout here with the picture and space for the case studies on the left. Somewhere beneath should be the 3 service areas with a picture each.
In terms of colors: our logo colours are Blue (RBG 8;44;80) and Orange (RGB 231;120;23). The orange could be used to emphasise certain things, however there should not be too much color.
Budget for images available, so please use placeholders or ask us for specific photos/images, if you need them for your design.
Updates
Hi, one more thing that we would like to have is the case studies not hidden behind a link "case studies" - we would like to have them individually linked prominent on the first page. There will be about 6-8 of them. Thats what we liked on the joomla template (the links left from the picture).
Hi, thanks very much for all the great proposals.
We are currently going through the selection process and will post our decision early next week.
Thanks again!
Liesel
Target Market(s)
- target customers are all different kinds of businesses and organisations (all industries, government, non-for-profit, ...) experiencing conflict and tension - be it with internal staff, amongst managers or board members, dysfunctional teams, between organizations or customers and organizations... examples could be bullying allegations, governmental negotiations with unions, disputes within organizations etc.
- also we will offer performance improvement services for organizations
- we will offer mediation, facilitation, negotiation, performance improvement services, conflict coaching, conflict management, change management services
- if comparable to anything - then to a law firm in terms of dealing with conflicts but its much less adversarial and much more about the people and their interests rather than about laws
- basically it's all kind of things you can do in order to solve disputes without involving lawyers and a court - so it's much cheaper and target is to find a solution all parties can live with rather than having a judge deciding about who wins and who looses
- performance management is more about analysing reasons for a lack of performance and setting up continous improvement systems, supporting change management, facilitating improvement workshops or strategic meetings, ...
Industry/Entity Type
Consulting
Look and feel

```html
<!DOCTYPE html>
<html lang="en">
<head>
<meta charset="utf-8">
<title>Halvern Ostrick — Conflict Resolution Consulting</title>
<link href="https://fonts.googleapis.com/css2?family=Didact+Gothic&display=swap" rel="stylesheet">
<style>
:root{
  --navy:#082c50;
  --navy-deep:#0a2a4c;
  --orange:#e77817;
  --white:#ffffff;
  --ink:#111111;
  --panel:rgba(8,44,80,.82);
  --display:"Didact Gothic",sans-serif;
  --body:Arial,Helvetica,sans-serif;
}
*{margin:0;padding:0;box-sizing:border-box}
html,body{width:784px;height:1200px;overflow:hidden;background:var(--white)}
body{position:relative;font-family:var(--body);color:var(--ink)}
.abs{position:absolute}

/* header */
.site-header{position:absolute;left:0;top:0;width:784px;height:79px}
.brand{left:26px;top:22px;display:flex;align-items:center;gap:8px}
.brand-name{font-family:var(--display);font-size:25px;color:var(--navy);letter-spacing:.5px}
.brand-mark{width:16px;height:16px;border:2px solid var(--orange)}
.brand-url{left:48px;top:58px;font-family:var(--display);font-size:10px;letter-spacing:6.2px;color:var(--navy)}
.call-label{right:30px;top:24px;font-family:var(--display);font-size:14px;color:var(--orange)}
.call-number{right:30px;top:40px;font-family:var(--display);font-size:28px;color:var(--navy);letter-spacing:-.5px}

/* nav */
.main-nav{position:absolute;left:0;top:79px;width:784px;height:38px;background:var(--navy);display:flex;align-items:center;padding-left:30px}
.main-nav a{font-family:var(--display);font-size:14px;color:var(--white);text-decoration:none;margin-right:28px}
.main-nav a:last-child{margin-right:0}

/* hero */
.hero{position:absolute;left:0;top:117px;width:784px;height:326px;
  background:linear-gradient(100deg,#3d6d8c 0%,#6c98b4 30%,#b8ccd9 55%,#5f84a0 80%,#8fb2c8 100%)}
.case-list{position:absolute;left:12px;top:41px;width:175px;height:285px;background:var(--panel);list-style:none;padding-top:12px}
.case-list li{height:32px;margin:0 0 0 16px;border-bottom:1px solid rgba(255,255,255,.12);display:flex;align-items:center;padding-left:13px;
  font-family:var(--display);font-size:12px;color:var(--white)}

/* services */
.services{position:absolute;left:0;top:443px;width:784px;height:268px;background:var(--orange)}
.service{position:absolute;top:18px;width:226px;text-align:center;color:var(--white)}
.service-photo{width:132px;height:132px;border-radius:50%;margin:0 auto;border:2px solid #f39a4b;background:radial-gradient(circle at 50% 40%,#e8eef3,#9fb3c4)}
.service h2{font-family:var(--display);font-weight:400;font-size:24px;margin-top:10px;letter-spacing:-.5px}
.service p{font-size:11px;line-height:13.6px;margin-top:8px}

/* why */
.why-title{left:27px;top:748px;font-family:var(--display);font-weight:400;font-size:29px;color:var(--ink)}
.why-photo{left:23px;top:800px;width:239px;height:160px;border:1px solid #d8d8d8;background:linear-gradient(135deg,#f2f2f2,#c9ccd3 50%,#f4e1d2 70%,#ececec)}
.why-text{left:277px;top:802px;width:468px;font-size:11.2px;line-height:13.5px;color:var(--ink)}
.why-text p+p{margin-top:13px}
.why-text .learn-more{display:inline-block;margin-top:12px;color:var(--orange);text-decoration:none}

/* footer */
.site-footer{position:absolute;left:0;top:1019px;width:784px;height:181px;background:var(--navy-deep);color:var(--white)}
.contact-title{left:20px;top:24px;font-size:14px}
.contact-note{left:19px;top:46px;width:400px;font-size:10px;line-height:11.5px}
.email-field{left:18px;top:75px;width:301px;height:27px;border:1px solid var(--orange);background:transparent}
.notify-btn{left:329px;top:75px;width:89px;height:27px;background:var(--orange);color:var(--navy);font-size:13px;display:flex;align-items:center;justify-content:center}
.loc-title{left:530px;top:25px;font-size:14px}
.loc-text{left:530px;top:45px;font-size:10px;line-height:11.5px}
.social{left:529px;top:95px;display:flex;gap:4px}
.social span{width:34px;height:34px;border-radius:50%;background:var(--orange)}
.footer-rule{left:0;top:139px;width:784px;height:1px;background:var(--orange)}
.footer-nav{left:19px;top:154px;display:flex;gap:8px;font-size:10px}
.footer-nav a{color:var(--white);text-decoration:none}
.footer-nav a.current{color:var(--orange)}
.copyright{right:67px;top:154px;font-size:9px;color:var(--orange)}
</style>
</head>
<body>

<header class="site-header">
  <div class="abs brand"><span class="brand-name">HALVERN OSTRICK</span><span class="brand-mark"></span></div>
  <div class="abs brand-url">www.kavilora.com.au</div>
  <div class="abs call-label">Contact us now. Toll Free!</div>
  <div class="abs call-number">013-246-5780</div>
</header>

<nav class="main-nav">
  <a href="#">Home</a><a href="#">Services</a><a href="#">Case Studies</a><a href="#">Engaging Us</a><a href="#">About Conflict</a><a href="#">Conflict Resolution</a><a href="#">About</a><a href="#">Contact</a>
</nav>

<section class="hero" role="img" aria-label="Photo of a smiling business team shaking hands in a glass office">
  <ul class="case-list">
    <li>Lorem ipsum dolor</li><li>Sit amet</li><li>Consectetur adipisicing</li><li>Sed do eiusmod</li><li>Tempor incididunt</li><li>Ut labore et</li><li>Dolore magna aliqua</li><li>Ut enim ad minim</li>
  </ul>
</section>

<section class="services">
  <div class="service" style="left:10px">
    <div class="service-photo" role="img" aria-label="Portrait photo of a thoughtful businesswoman"></div>
    <h2>Improvement</h2>
    <p>Lorem ipsum dolor sit amet, consectetur adipisicing elit, sed do eiusmod tempor incididunt ut labore et .</p>
  </div>
  <div class="service" style="left:263px">
    <div class="service-photo" role="img" aria-label="Photo of a coaching session at a desk"></div>
    <h2>Coaching</h2>
    <p>Sed ut perspiciatis, unde omnis iste natus error sit voluptatem accusantium doloremque laudantium, totam rem aperiam eaque</p>
  </div>
  <div class="service" style="left:537px">
    <div class="service-photo" role="img" aria-label="Portrait photo of a smiling manager"></div>
    <h2>Management</h2>
    <p>Sed ut perspiciatis, unde omnis iste natus error sit voluptatem accusantium doloremque laudantium, totam rem aperiam eaque</p>
  </div>
</section>

<h1 class="abs why-title">Why Choose Halvern Ostrick?</h1>
<div class="abs why-photo" role="img" aria-label="Photo of a handshake in front of a crowd of people"></div>
<div class="abs why-text">
  <p>Lorem ipsum dolor sit amet, consectetur adipisicing elit, sed do eiusmod tempor incididunt ut labore et dolore magna aliqua. Ut enim ad minim veniam, quis nostrud exercitation ullamco laboris nisi ut aliquip ex ea commodo consequat. Duis aute irure dolor in reprehenderit in voluptate velit esse cillum dolore eu fugiat nulla pariatur. Excepteur sint occaecat cupidatat non proident, sunt in culpa qui officia deserunt mollit anim id est laborum.</p>
  <p>Sed ut perspiciatis, unde omnis iste natus error sit voluptatem accusantium doloremque laudantium, totam rem aperiam eaque ipsa, quae ab illo inventore veritatis et quasi architecto beatae vitae dicta sunt, explicabo.</p>
  <a class="learn-more" href="#">learn more</a>
</div>

<footer class="site-footer">
  <div class="abs contact-title"><b>Feel free</b> to contact us</div>
  <div class="abs contact-note">At vero eos et accusamus et iusto odio dignissimos ducimus, qui blanditiis praesentium voluptatum deleniti atque corrupti, quos dolores et quas molestias excepturi sint."</div>
  <div class="abs email-field"></div>
  <div class="abs notify-btn">Notify me</div>
  <div class="abs loc-title"><b>Our</b> location</div>
  <div class="abs loc-text">27 Corvale Lane<br>Brenmouth, K12 7TQ.<br>Phone: +1 555 204 3318</div>
  <div class="abs social" aria-label="Social links"><span></span><span></span><span></span><span></span><span></span></div>
  <div class="abs footer-rule"></div>
  <div class="abs footer-nav"><a class="current" href="#">Home</a><a href="#">Services</a><a href="#">Case Studies</a><a href="#">Engaging Us</a><a href="#">About Conflict</a><a href="#">Conflict Resolution</a><a href="#">About</a><a href="#">Contact</a></div>
  <div class="abs copyright"><b>Company Name</b> © 2013. All Rights Reserved</div>
</footer>

</body>
</html>
```